Swiss Consultant for Enterprises and SME's is in Need for PPT for Teaching/Presenting

I am looking for a powerpointpresentation template (must be with slidemaster) for presenting my company and also for teaching. Colors must be taken from Logo and content can be taken from website if needed.

It is either used to present anything regarding finances and ERP-Systemrelated topics (espeically VEX Trade Suite) and also teach anything regarding Finance and or ERP-Systems in an industrial or financial environment.
Updates

Low design quality

Font styles to use
Sans Serif

Requirements
Must have
• I need at least following slides (Title, Subtitle/Section, Index, Single content, Empty (just logo), two content, tree content -> each as column and at last 4 / 5 & 6 infographics (done with o365 "standard" Icons)
• Coloring white and same as logo provided no additional colors except for charts etc.(matching to logostyle)
• Also I need a Word template such as the one attached.
Nice to have
• any additional infographic
Should not have
• Presentation must be done in the slidemaster as a template anything else will not be accepted.
• Letterhead is not needed I only need a Document for Documentation.

```html
<!DOCTYPE html>
<html lang="en">
<head>
<meta charset="utf-8">
<title>Kessler Consulting – Presentation Template</title>
<link rel="stylesheet" href="https://fonts.googleapis.com/css2?family=Montserrat:wght@400;600;700;800&family=Open+Sans:wght@400;600&display=swap">
<style>
:root{
  --blue:#2f6cb5;
  --blue-dark:#1f4f8c;
  --yellow:#ffe81a;
  --ink:#1b1b1b;
  --grey:#6b6b6b;
  --paper:#ffffff;
  --line:#e3e3e3;
}
*{box-sizing:border-box;margin:0;padding:0}
html,body{width:1200px;height:2203px;overflow:hidden;background:var(--paper)}
body{position:relative;font-family:"Open Sans",Arial,sans-serif;color:var(--ink)}
.slide{position:absolute;width:534px;height:300px;overflow:hidden;background:var(--paper);box-shadow:0 1px 4px rgba(0,0,0,.28)}
.col-l{left:32px}.col-r{left:632px}
.row1{top:22px}.row2{top:383px}.row3{top:740px}.row4{top:1105px}.row5{top:1472px}.row6{top:1832px}
.caption{position:absolute;width:534px;text-align:center;font-family:"Open Sans",Arial,sans-serif;font-size:20px;color:var(--ink);letter-spacing:.3px}
.abs{position:absolute}
.photo{position:absolute}
.brand{display:flex;align-items:center;justify-content:center;gap:5px;font-family:"Montserrat",Arial,sans-serif;font-weight:700;color:var(--blue);white-space:nowrap}
.brand .mark{width:7px;height:7px;background:var(--yellow)}
.brand-corner{position:absolute;right:12px;top:17px;font-size:8px}
.brand-corner .mark{width:4px;height:4px}
.slide-title{position:absolute;left:16px;top:18px;font-family:"Montserrat",Arial,sans-serif;font-size:9px;font-weight:400;color:var(--ink)}
.slide-title b{font-weight:700}
.rule{position:absolute;left:0;right:26px;bottom:15px;height:1.5px;background:var(--yellow)}
.page-num{position:absolute;right:8px;bottom:7px;width:16px;height:16px;border-radius:50%;background:var(--yellow);font-family:"Montserrat",Arial,sans-serif;font-size:6px;font-weight:600;display:flex;align-items:center;justify-content:center;color:var(--ink)}
.body-text{font-size:5.6px;line-height:1.55;color:var(--grey)}
.frame{position:absolute;border:4px solid var(--yellow)}
.white-box{position:absolute;background:var(--paper);display:flex;flex-direction:column;align-items:center;justify-content:center}
.yellow-band{position:absolute;background:var(--yellow);display:flex;flex-direction:column;align-items:center;justify-content:center}
.band-title{font-family:"Montserrat",Arial,sans-serif;font-size:21px;font-weight:800;color:var(--ink);letter-spacing:.3px}
.band-title span{font-weight:400}
.band-url{font-family:"Montserrat",Arial,sans-serif;font-size:6.5px;letter-spacing:2px;color:var(--ink);margin-top:2px}
.alpine{background:linear-gradient(180deg,#1c63b4 0%,#3f82c8 38%,#8fa6bb 62%,#d4d8dc 80%,#eceeef 100%)}

/* page 01 */
.point{position:absolute;left:285px;width:230px;display:flex;gap:8px}
.point-badge{flex:none;width:26px;height:26px;border-radius:50%;background:var(--yellow);font-family:"Montserrat",Arial,sans-serif;font-weight:700;font-size:11px;display:flex;align-items:center;justify-content:center;color:var(--ink)}
.point-head{font-family:"Montserrat",Arial,sans-serif;font-size:9px;color:#fff;margin-top:-1px}
.point-text{font-size:5.3px;line-height:1.45;color:#e6e6e6;width:190px}

/* page 05 */
.service{position:absolute;top:83px;width:100px;text-align:center}
.service-box{width:100px;height:94px;border:2px solid var(--blue);border-radius:3px;display:flex;align-items:center;justify-content:center;background:var(--paper)}
.service-box.is-active{background:var(--blue)}
.service .body-text{margin-top:12px;text-align:center;padding:0 4px}

/* page 06 */
.split-title{position:absolute;top:44px;font-family:"Montserrat",Arial,sans-serif;font-size:16px;white-space:nowrap}
.split-title.is-light{right:272px;font-weight:700;color:#fff}
.split-title.is-dark{left:272px;font-weight:400;color:var(--ink)}
.check-item{position:absolute;left:316px;display:flex;gap:12px;align-items:flex-start}
.check-dot{flex:none;width:22px;height:22px;border-radius:50%;background:var(--yellow);display:flex;align-items:center;justify-content:center}
.check-head{font-family:"Montserrat",Arial,sans-serif;font-size:8.5px;color:var(--ink)}
.check-text{font-size:5.5px;color:var(--grey);margin-top:1px}

/* page 07 */
.step-text{position:absolute;width:100px;text-align:center}
.step-head{font-family:"Montserrat",Arial,sans-serif;font-size:5.8px;color:var(--ink);margin-bottom:6px}
.step-num{position:absolute;font-size:6px;color:var(--ink)}

/* page 08 */
.tile{position:absolute;width:70px;height:70px;background:var(--blue);border-radius:8px;transform:rotate(45deg)}
.tile-num{position:absolute;width:70px;text-align:center;font-family:"Montserrat",Arial,sans-serif;font-weight:600;font-size:22px;color:#fff}
.stat{position:absolute;left:310px;display:flex;gap:14px;align-items:center}
.stat-head{font-family:"Montserrat",Arial,sans-serif;font-size:8.5px;color:var(--ink)}

/* page 09 */
.gallery-item{position:absolute;width:80px;text-align:center}
.gallery-head{font-family:"Montserrat",Arial,sans-serif;font-size:5.8px;color:var(--ink);margin:0 0 5px}

/* back page */
.contact-head{font-family:"Montserrat",Arial,sans-serif;font-size:8px;font-weight:700;color:var(--ink)}
.contact-icons{display:flex;gap:4px;margin:5px 0 6px}
.contact-icons i{width:7px;height:7px;border-radius:50%;background:var(--blue);display:block}
.contact-line{font-size:5.8px;color:var(--ink);line-height:1.6}

.brand-hero{position:absolute;left:700px;top:1955px;width:400px;font-size:42px;gap:14px}
.brand-hero .mark{width:22px;height:22px}
</style>
</head>
<body>

<!-- Cover -->
<section class="slide col-l row1">
  <div class="photo alpine" style="inset:0" role="img" aria-label="Photo of a snow-covered alpine peak under a deep blue sky"></div>
  <div class="frame" style="left:165px;top:51px;width:201px;height:242px"></div>
  <div class="white-box" style="left:172px;top:58px;width:187px;height:81px">
    <div class="brand" style="font-size:14px"><span>Kessler Consulting</span><span class="mark"></span></div>
  </div>
  <div class="yellow-band" style="left:113px;top:139px;width:310px;height:69px">
    <div class="band-title">PRESENTATION <span>TITLE</span></div>
    <div class="band-url">www.kessler-consulting.ch</div>
  </div>
</section>
<div class="caption col-l" style="top:336px">COVER PAGE</div>

<!-- Page 01 -->
<section class="slide col-r row1" style="background:#111">
  <div class="photo" style="inset:0;background:radial-gradient(ellipse at 22% 55%,#4a4d52 0%,#26282b 35%,#101112 70%)" role="img" aria-label="Photo of a businessman in a dark suit offering a handshake"></div>
  <div class="point" style="top:37px"><span class="point-badge">A</span><div><div class="point-head">LOREM IPSUM</div><div class="point-text">Lorem Ipsum is simply dummy text of the printing and typesetting industry. Lorem Ipsum has been the industry's.</div></div></div>
  <div class="point" style="top:95px"><span class="point-badge">B</span><div><div class="point-head">LOREM IPSUM</div><div class="point-text">Lorem Ipsum is simply dummy text of the printing and typesetting industry. Lorem Ipsum has been the industry's.</div></div></div>
  <div class="point" style="top:154px"><span class="point-badge">C</span><div><div class="point-head">LOREM IPSUM</div><div class="point-text">Lorem Ipsum is simply dummy text of the printing and typesetting industry. Lorem Ipsum has been the industry's.</div></div></div>
  <div class="point" style="top:212px"><span class="point-badge">D</span><div><div class="point-head">LOREM IPSUM</div><div class="point-text">Lorem Ipsum is simply dummy text of the printing and typesetting industry. Lorem Ipsum has been the industry's.</div></div></div>
  <div class="rule"></div><div class="page-num">01</div>
</section>
<div class="caption col-r" style="top:336px">PAGE - 01</div>

<!-- Page 02 -->
<section class="slide col-l row2" style="background:#2a211a">
  <div class="photo" style="inset:0;background:linear-gradient(120deg,#3a2f26 0%,#5a4634 35%,#7c6a58 55%,#c9c4bb 75%,#8a847b 100%)" role="img" aria-label="Photo of hands on a laptop beside a person reading a business newspaper"></div>
  <div class="frame" style="left:114px;top:63px;width:309px;height:153px;border-width:3px"></div>
  <div class="white-box" style="left:133px;top:82px;width:271px;height:127px">
    <div class="brand" style="font-size:24px;gap:8px"><span>Kessler Consulting</span><span class="mark" style="width:11px;height:11px"></span></div>
  </div>
  <div class="rule"></div><div class="page-num">02</div>
</section>
<div class="caption col-l" style="top:697px">PAGE - 02</div>

<!-- Page 03 -->
<section class="slide col-r row2">
  <div class="photo" style="left:0;top:0;width:534px;height:151px;background:linear-gradient(90deg,#d88f00 0%,#f4bd12 18%,#f7cc33 30%,#3b342c 42%,#6d655c 60%,#8a8177 78%,#3a3633 100%)" role="img" aria-label="Photo of two silhouetted business people in front of a glowing yellow wall"></div>
  <div class="abs" style="left:0;top:151px;width:534px;height:149px;background:var(--blue)"></div>
  <div class="frame" style="left:82px;top:50px;width:405px;height:212px;border-width:3px"></div>
  <div class="abs" style="left:202px;top:116px;font-family:'Montserrat',Arial,sans-serif;font-size:15px;color:#fff">LOREM IPSUM</div>
  <p class="abs body-text" style="left:107px;top:199px;width:322px;color:#fff;text-align:justify">Lorem Ipsum is simply dummy text of the printing and typesetting industry. Lorem Ipsum has been the industry's standard dummy text ever since the 1500s, when an unknown printer took a galley of type and scrambled it to make a type specimen book. It has survived not only five centuries, but also the leap into electronic typesetting, remaining essentially unchanged.</p>
  <div class="page-num">03</div>
</section>
<div class="caption col-r" style="top:697px">PAGE - 03</div>

<!-- Page 04 -->
<section class="slide col-l row3">
  <div class="slide-title"><b>LOREM</b> IPSUM</div>
  <p class="abs body-text" style="left:16px;top:62px;width:164px;text-align:justify">Lorem Ipsum is simply dummy text of the printing and typesetting industry. Lorem Ipsum has been the industry's standard dummy text ever since the 1500s, when an unknown printer took a galley of type and scrambled it to make a type specimen book. It has survived not only five centuries, but also the leap into electronic typesetting, remaining essentially unchanged. It was popularised in the 1960s with the release of Letraset sheets.</p>
  <p class="abs body-text" style="left:16px;top:172px;width:164px;text-align:justify">Lorem Ipsum is simply dummy text of the printing and typesetting industry. Lorem Ipsum has been the industry's standard dummy text ever since the 1500s, when an unknown printer took a galley of type and scrambled it to make a type specimen book. It has survived not only five centuries, but also the leap into electronic typesetting, remaining essentially unchanged. It was popularised in the 1960s with the release of Letraset sheets.</p>
  <div class="photo" style="left:212px;top:67px;width:166px;height:233px;background:linear-gradient(160deg,#3b4a5e 0%,#1d2631 45%,#4d5866 75%,#262c33 100%)" role="img" aria-label="Photo of hands typing on a laptop"></div>
  <div class="photo" style="left:385px;top:0;width:149px;height:237px;background:linear-gradient(180deg,#2d2d2d 0%,#4b5a70 40%,#5878a6 65%,#2a2f38 100%)" role="img" aria-label="Photo of a young man in a denim shirt taking notes"></div>
  <div class="rule" style="right:auto;width:212px"></div><div class="page-num">04</div>
</section>
<div class="caption col-l" style="top:1053px">PAGE - 04</div>

<!-- Page 05 -->
<section class="slide col-r row3">
  <div class="slide-title"><b>LOREM</b> IPSUM</div>
  <div class="brand brand-corner"><span>Kessler Consulting</span><span class="mark"></span></div>
  <div class="service" style="left:51px">
    <div class="service-box">
      <svg width="48" height="48" viewBox="0 0 48 48"><circle cx="12" cy="12" r="4" fill="#1b1b1b"/><circle cx="36" cy="12" r="4" fill="#1b1b1b"/><path d="M6 30v-8a6 6 0 0 1 12 0v8zM30 30v-8a6 6 0 0 1 12 0v8z" fill="#1b1b1b"/><rect x="14" y="24" width="20" height="3" fill="#1b1b1b"/><rect x="22" y="27" width="4" height="14" fill="#1b1b1b"/><rect x="8" y="30" width="3" height="11" fill="#1b1b1b"/><rect x="37" y="30" width="3" height="11" fill="#1b1b1b"/></svg>
    </div>
    <p class="body-text">Lorem Ipsum is simply dummy text of the printing and typesetting industry. Lorem Ipsum has been the industry's standard dummy text ever since the 1500s, when an unknown.</p>
  </div>
  <div class="service" style="left:218px">
    <div class="service-box is-active">
      <svg width="48" height="48" viewBox="0 0 48 48"><circle cx="24" cy="13" r="5" fill="#fff"/><path d="M15 30v-6a9 9 0 0 1 18 0v6z" fill="#fff"/><rect x="14" y="24" width="20" height="10" rx="1" fill="none" stroke="#fff" stroke-width="2"/><rect x="9" y="35" width="30" height="3" fill="#fff"/></svg>
    </div>
    <p class="body-text">Lorem Ipsum is simply dummy text of the printing and typesetting industry. Lorem Ipsum has been the industry's standard dummy text ever since the 1500s, when an unknown.</p>
  </div>
  <div class="service" style="left:379px">
    <div class="service-box">
      <svg width="48" height="48" viewBox="0 0 48 48"><circle cx="20" cy="16" r="6" fill="#1b1b1b"/><path d="M8 42v-8a12 10 0 0 1 24 0v8z" fill="#1b1b1b"/><path d="M20 26l-2 6 2 6 2-6z" fill="#fff"/><path d="M30 6h12v9h-7l-3 3v-3h-2z" fill="none" stroke="#1b1b1b" stroke-width="2"/></svg>
    </div>
    <p class="body-text">Lorem Ipsum is simply dummy text of the printing and typesetting industry. Lorem Ipsum has been the industry's standard dummy text ever since the 1500s, when an unknown.</p>
  </div>
  <div class="rule"></div><div class="page-num">05</div>
</section>
<div class="caption col-r" style="top:1053px">PAGE - 05</div>

<!-- Page 06 -->
<section class="slide col-l row4">
  <div class="photo" style="left:0;top:0;width:268px;height:300px;background:linear-gradient(135deg,#2b2622 0%,#5a4c40 35%,#8a7763 55%,#c9c3bb 75%,#3f5f8f 100%)" role="img" aria-label="Photo of a person writing in a notebook beside a laptop"></div>
  <div class="split-title is-light">LOREM</div>
  <div class="split-title is-dark">IPSUM</div>
  <div class="brand brand-corner"><span>Kessler Consulting</span><span class="mark"></span></div>
  <div class="check-item" style="top:90px"><span class="check-dot"><svg width="12" height="12" viewBox="0 0 12 12"><circle cx="4" cy="3.5" r="1.6" fill="#1b1b1b"/><circle cx="8" cy="3.5" r="1.6" fill="#1b1b1b"/><rect x="2" y="6" width="8" height="4" rx="1" fill="#1b1b1b"/></svg></span><div><div class="check-head">LOREM IPSUM</div><div class="check-text">Lorem Ipsum is simply dummy text of the printing.</div></div></div>
  <div class="check-item" style="top:134px"><span class="check-dot"><svg width="12" height="12" viewBox="0 0 12 12"><circle cx="6" cy="3.5" r="2" fill="#1b1b1b"/><rect x="2.5" y="6.5" width="7" height="4" rx="1" fill="#1b1b1b"/></svg></span><div><div class="check-head">LOREM IPSUM</div><div class="check-text">Lorem Ipsum is simply dummy text of the printing.</div></div></div>
  <div class="check-item" style="top:178px"><span class="check-dot"><svg width="12" height="12" viewBox="0 0 12 12"><circle cx="5" cy="4" r="2" fill="#1b1b1b"/><rect x="1.5" y="7" width="7" height="4" rx="1" fill="#1b1b1b"/><rect x="8" y="1" width="3.5" height="3" fill="#1b1b1b"/></svg></span><div><div class="check-head">LOREM IPSUM</div><div class="check-text">Lorem Ipsum is simply dummy text of the printing.</div></div></div>
  <div class="check-item" style="top:222px"><span class="check-dot"><svg width="12" height="12" viewBox="0 0 12 12"><circle cx="3" cy="4" r="1.5" fill="#1b1b1b"/><circle cx="6" cy="3" r="1.7" fill="#1b1b1b"/><circle cx="9" cy="4" r="1.5" fill="#1b1b1b"/><rect x="1" y="6.5" width="10" height="4" rx="1" fill="#1b1b1b"/></svg></span><div><div class="check-head">LOREM IPSUM</div><div class="check-text">Lorem Ipsum is simply dummy text of the printing.</div></div></div>
  <div class="rule" style="left:268px"></div><div class="page-num">06</div>
</section>
<div class="caption col-l" style="top:1417px">PAGE - 06</div>

<!-- Page 07 -->
<section class="slide col-r row4">
  <div class="slide-title"><b>LOREM</b> IPSUM</div>
  <div class="brand brand-corner"><span>Kessler Consulting</span><span class="mark"></span></div>
  <svg class="abs" style="left:0;top:0" width="534" height="300" viewBox="0 0 534 300">
    <line x1="88" y1="161" x2="443" y2="161" stroke="#555" stroke-width="1"/>
    <g fill="#555"><circle cx="88" cy="161" r="2"/><circle cx="211" cy="161" r="2"/><circle cx="325" cy="161" r="2"/><circle cx="443" cy="161" r="2"/></g>
    <g stroke="var(--blue)" stroke-width="2" fill="#fff">
      <circle cx="211" cy="111" r="40"/><circle cx="443" cy="111" r="40"/><circle cx="88" cy="214" r="40"/><circle cx="325" cy="214" r="40"/>
    </g>
    <g fill="var(--blue)">
      <circle cx="211" cy="111" r="33"/><circle cx="443" cy="111" r="33"/><circle cx="88" cy="214" r="33"/><circle cx="325" cy="214" r="33"/>
    </g>
    <g fill="#fff">
      <circle cx="201" cy="102" r="4"/><circle cx="221" cy="102" r="4"/><rect x="194" y="108" width="14" height="10" rx="3"/><rect x="214" y="108" width="14" height="10" rx="3"/><rect x="200" y="119" width="22" height="3"/>
      <circle cx="443" cy="98" r="4"/><circle cx="433" cy="104" r="3.5"/><circle cx="453" cy="104" r="3.5"/><rect x="437" y="104" width="12" height="18" rx="3"/><rect x="427" y="110" width="10" height="12" rx="3"/><rect x="449" y="110" width="10" height="12" rx="3"/>
      <circle cx="88" cy="203" r="5"/><rect x="79" y="210" width="18" height="10" rx="3"/><rect x="74" y="221" width="28" height="3"/>
      <circle cx="322" cy="205" r="6"/><rect x="311" y="213" width="22" height="14" rx="4"/><path d="M331 195h12v8h-6l-3 3v-3h-3z"/>
    </g>
  </svg>
  <span class="step-num" style="left:84px;top:149px">01</span>
  <span class="step-num" style="left:207px;top:166px">02</span>
  <span class="step-num" style="left:321px;top:149px">03</span>
  <span class="step-num" style="left:439px;top:166px">04</span>
  <div class="step-text" style="left:38px;top:90px"><div class="step-head">LOREM IPSUM</div><p class="body-text">Lorem Ipsum is simply dummy text of the printing and typesetting industry.</p></div>
  <div class="step-text" style="left:275px;top:90px"><div class="step-head">LOREM IPSUM</div><p class="body-text">Lorem Ipsum is simply dummy text of the printing and typesetting industry.</p></div>
  <div class="step-text" style="left:161px;top:192px"><div class="step-head">LOREM IPSUM</div><p class="body-text">Lorem Ipsum is simply dummy text of the printing and typesetting industry.</p></div>
  <div class="step-text" style="left:393px;top:192px"><div class="step-head">LOREM IPSUM</div><p class="body-text">Lorem Ipsum is simply dummy text of the printing and typesetting industry.</p></div>
  <div class="rule"></div><div class="page-num">07</div>
</section>
<div class="caption col-r" style="top:1417px">PAGE - 07</div>

<!-- Page 08 -->
<section class="slide col-l row5">
  <div class="slide-title"><b>LOREM</b> IPSUM</div>
  <div class="brand brand-corner"><span>Kessler Consulting</span><span class="mark"></span></div>
  <div class="tile" style="left:113px;top:97px"></div>
  <div class="tile" style="left:54px;top:154px"></div>
  <div class="tile" style="left:171px;top:154px"></div>
  <div class="tile-num" style="left:113px;top:116px">01</div>
  <div class="tile-num" style="left:54px;top:173px">03</div>
  <div class="tile-num" style="left:171px;top:173px">02</div>
  <div class="stat" style="top:82px">
    <svg width="30" height="30" viewBox="0 0 30 30"><circle cx="15" cy="15" r="14" fill="#fff" stroke="var(--blue)" stroke-width="1"/><path d="M15 15V1A14 14 0 0 1 23.2 26.3z" fill="var(--blue)"/><text x="4" y="17" font-size="5" fill="#555" font-family="Open Sans, sans-serif">40%</text></svg>
    <div><div class="stat-head">LOREM IPSUM</div><div class="body-text">Lorem Ipsum is simply dummy text of the printing.</div></div>
  </div>
  <div class="stat" style="top:143px">
    <svg width="30" height="30" viewBox="0 0 30 30"><circle cx="15" cy="15" r="14" fill="#fff" stroke="var(--blue)" stroke-width="1"/><path d="M15 15V1A14 14 0 0 1 26.3 6.8z" fill="var(--blue)"/><text x="10" y="24" font-size="5" fill="#555" font-family="Open Sans, sans-serif">15%</text></svg>
    <div><div class="stat-head">LOREM IPSUM</div><div class="body-text">Lorem Ipsum is simply dummy text of the printing.</div></div>
  </div>
  <div class="stat" style="top:206px">
    <svg width="30" height="30" viewBox="0 0 30 30"><circle cx="15" cy="15" r="14" fill="#fff" stroke="var(--blue)" stroke-width="1"/><path d="M15 15V1A14 14 0 0 1 28.3 19.3z" fill="var(--blue)"/><text x="5" y="17" font-size="5" fill="#555" font-family="Open Sans, sans-serif">70%</text></svg>
    <div><div class="stat-head">LOREM IPSUM</div><div class="body-text">Lorem Ipsum is simply dummy text of the printing.</div></div>
  </div>
  <div class="rule"></div><div class="page-num">08</div>
</section>
<div class="caption col-l" style="top:1781px">PAGE - 08</div>

<!-- Page 09 -->
<section class="slide col-r row5">
  <div class="slide-title"><b>LOREM</b> IPSUM</div>
  <div class="brand brand-corner"><span>Kessler Consulting</span><span class="mark"></span></div>
  <svg class="abs" style="left:0;top:0" width="534" height="200" viewBox="0 0 534 200">
    <g fill="none" stroke="var(--blue)" stroke-width="2">
      <path d="M88 72l43 43-43 43-43-43z"/><path d="M207 72l43 43-43 43-43-43z"/><path d="M327 72l43 43-43 43-43-43z"/><path d="M447 72l43 43-43 43-43-43z"/>
    </g>
    <g role="img" aria-label="Four diamond photo crops: hands typing, a writing hand, a smiling woman at a laptop, and a workspace seen from above">
      <path d="M85 79l39 39-39 39-39-39z" fill="#6f7d8c"/>
      <path d="M204 79l39 39-39 39-39-39z" fill="#5c5249"/>
      <path d="M324 79l39 39-39 39-39-39z" fill="#b9aca0"/>
      <path d="M444 79l39 39-39 39-39-39z" fill="#6b4e36"/>
    </g>
  </svg>
  <div class="gallery-item" style="left:45px;top:196px"><div class="gallery-head">LOREM IPSUM</div><p class="body-text">Lorem Ipsum is simply dummy text of the printing and typesetting industry.</p></div>
  <div class="gallery-item" style="left:164px;top:196px"><div class="gallery-head">LOREM IPSUM</div><p class="body-text">Lorem Ipsum is simply dummy text of the printing and typesetting industry.</p></div>
  <div class="gallery-item" style="left:284px;top:196px"><div class="gallery-head">LOREM IPSUM</div><p class="body-text">Lorem Ipsum is simply dummy text of the printing and typesetting industry.</p></div>
  <div class="gallery-item" style="left:404px;top:196px"><div class="gallery-head">LOREM IPSUM</div><p class="body-text">Lorem Ipsum is simply dummy text of the printing and typesetting industry.</p></div>
  <div class="rule"></div><div class="page-num">09</div>
</section>
<div class="caption col-r" style="top:1781px">PAGE - 09</div>

<!-- Back page -->
<section class="slide col-l row6">
  <div class="photo alpine" style="inset:0" role="img" aria-label="Photo of snowy alpine mountains under a blue sky"></div>
  <div class="frame" style="left:165px;top:26px;width:201px;height:249px"></div>
  <div class="white-box" style="left:172px;top:33px;width:187px;height:81px">
    <div class="contact-head">CONTACT US</div>
    <div class="contact-icons"><i></i><i></i></div>
    <div class="contact-line">Birkenweg 12, 3600 Thun</div>
    <div class="contact-line">info@kessler-consulting.ch</div>
  </div>
  <div class="yellow-band" style="left:113px;top:114px;width:310px;height:70px">
    <div class="band-title">THANK YOU</div>
    <div class="band-url">www.kessler-consulting.ch</div>
  </div>
  <div class="white-box" style="left:172px;top:184px;width:187px;height:84px">
    <div class="brand" style="font-size:14px"><span>Kessler Consulting</span><span class="mark"></span></div>
  </div>
</section>
<div class="caption col-l" style="top:2142px">BACK PAGE</div>

<div class="brand brand-hero"><span>Kessler Consulting</span><span class="mark"></span></div>

</body>
</html>
```